Camp Brambleton Day Camp Brochure

I need someone to design a brochure for our day camp. It will be 8.5 x 11 inch paper folded horizontally. Looking for a fun, clean design. I sent several pictures, not all of them have to be used. The brochure will be mailed out to former day campers and used at events to help us market our program. A colorful brochure would be nice. I would like the cover page to be portrait along with the two inside pages. The back cover will need to be landscape format.

Target Market(s)

Parents

Colors

Designer to choose colors to be used in the design.

Requirements
Must have
• All information provided. Great design on the inside pages

```html
<!DOCTYPE html>
<html lang="en">
<head>
<meta charset="utf-8">
<title>Camp Brambleton Day Camp 2019 Brochure</title>
<link rel="stylesheet" href="https://fonts.googleapis.com/css2?family=Montserrat:wght@400;600;700;800&family=Oswald:wght@600;700&display=swap">
<style>
  :root{
    --red:#9b0b10;
    --red-bright:#d8141b;
    --gold:#e39a14;
    --ink:#333333;
    --muted:#cfcfcf;
    --paper:#ffffff;
    --stage:#6a6a6a;
    --box:#e6e6e6;
  }
  *{box-sizing:border-box;margin:0;padding:0}
  html,body{width:1200px;height:2731px;overflow:hidden;background:var(--stage)}
  body{font-family:"Montserrat",Arial,sans-serif;color:var(--ink)}
  .canvas{position:relative;width:1200px;height:2731px;overflow:hidden;background:var(--stage)}
  .spread{position:absolute;left:50px;width:1100px;height:850px;overflow:hidden;box-shadow:0 10px 30px rgba(0,0,0,.35)}
  .spread--outside{top:455px}
  .spread--inside{top:1405px}
  .spread svg.art{position:absolute;inset:0;width:1100px;height:850px}
  .layer{position:absolute}

  /* outside */
  .back-brand{left:40px;top:36px;font-size:28px;font-weight:800;color:var(--muted);letter-spacing:.5px}
  .mailing{left:113px;top:322px;width:400px;text-align:center}
  .mailing__line{font-size:20px;font-weight:800;line-height:25px;color:var(--ink)}
  .mailing__phone{display:flex;justify-content:center;align-items:center;gap:8px;margin-top:12px}
  .phone-icon{width:32px;height:32px;border-radius:7px;background:var(--gold);display:flex;align-items:center;justify-content:center}
  .phone-pill{background:var(--red-bright);color:#fff;font-weight:800;font-size:22px;padding:3px 16px;border-radius:8px}
  .mailing__email{margin-top:10px;font-size:14px;font-weight:600}
  .cover-brand{left:700px;top:38px;width:360px;text-align:right;font-size:28px;font-weight:800;color:var(--red);letter-spacing:.5px}
  .cover-title{left:700px;top:770px;width:320px;text-align:center;color:#fff}
  .cover-title__kicker{font-size:17px;font-weight:800;letter-spacing:.5px}
  .cover-title__main{font-family:"Oswald",Impact,sans-serif;font-size:50px;font-weight:700;line-height:54px}

  /* inside */
  .intro{left:42px;top:268px;width:490px;font-size:12px;line-height:16px}
  .intro p{margin-bottom:8px}
  .details{left:232px;top:372px;width:310px;font-size:12px;line-height:16px}
  .details p{margin-bottom:8px}
  .price{color:var(--gold);font-weight:800;font-size:15px;line-height:20px}
  .heading-red{color:var(--red-bright);font-weight:800;font-size:13px;text-decoration:underline;margin-bottom:5px}
  .stops{left:232px;top:605px;width:310px}
  .stop{display:flex;justify-content:space-between;font-size:11px;font-weight:700;line-height:16px}
  .discounts{left:595px;top:168px;width:470px;font-size:13px;line-height:18px}
  .weeks{left:595px;top:305px;width:483px;height:208px;background:var(--box);border-radius:16px;text-align:center;padding:12px}
  .weeks__note{font-size:12px;color:#555;margin-bottom:6px}
  .weeks__title{font-weight:800;color:var(--red-bright);font-size:15px;margin-bottom:4px}
  .weeks__list{list-style:none;font-size:12px;font-weight:700;line-height:15.5px}
  .register{left:585px;top:532px;width:503px;text-align:center}
  .register__cta{color:var(--red-bright);font-weight:800;font-size:17px;white-space:nowrap}
  .register__note{font-weight:800;font-size:13px;margin-top:4px}
</style>
</head>
<body>
<main class="canvas">

  <section class="spread spread--outside">
    <svg class="art" viewBox="0 0 1100 850">
      <defs>
        <linearGradient id="paper" x1="0" y1="0" x2="1" y2="1">
          <stop offset="0" stop-color="#ffffff"/><stop offset="1" stop-color="#e2e2e2"/>
        </linearGradient>
        <linearGradient id="riderPhoto" x1="0" y1="0" x2="1" y2="1">
          <stop offset="0" stop-color="#3f5e2f"/><stop offset=".45" stop-color="#86a05a"/>
          <stop offset=".7" stop-color="#c95a6a"/><stop offset="1" stop-color="#b9a98a"/>
        </linearGradient>
      </defs>
      <rect width="1100" height="850" fill="url(#paper)"/>
      <g role="img" aria-label="Photo of a smiling girl in a helmet riding a horse among trees">
        <path d="M550,140 C700,112 900,74 1100,62 V760 H550 Z" fill="url(#riderPhoto)"/>
      </g>
      <path d="M550,128 C700,100 900,62 1100,50 V62 C900,74 700,112 550,140 Z" fill="var(--gold)"/>
      <path d="M0,100 C200,100 400,70 550,30 V42 C400,82 200,112 0,112 Z" fill="var(--red)"/>
      <path d="M0,116 C200,116 400,88 550,48 V62 C400,102 200,132 0,132 Z" fill="var(--gold)"/>
      <rect x="445" y="117" width="68" height="64" fill="#fff" stroke="#9a9a9a"/>
      <text x="479" y="134" font-size="7" font-family="Montserrat, sans-serif" font-weight="700" text-anchor="middle" fill="#555">NONPROFIT ORG</text>
      <text x="479" y="146" font-size="7" font-family="Montserrat, sans-serif" font-weight="700" text-anchor="middle" fill="#555">U.S. POSTAGE</text>
      <text x="479" y="158" font-size="7" font-family="Montserrat, sans-serif" font-weight="700" text-anchor="middle" fill="#555">PAID</text>
      <text x="479" y="170" font-size="7" font-family="Montserrat, sans-serif" font-weight="700" text-anchor="middle" fill="#555">PERMIT NO. 12</text>
      <rect x="80" y="485" width="390" height="130" rx="18" fill="#fff" stroke="#dcdcdc" stroke-width="2"/>
      <path d="M0,700 C300,690 650,770 1100,690 V850 H0 Z" fill="var(--gold)"/>
      <path d="M0,737 C300,727 650,795 1100,737" fill="none" stroke="#fff" stroke-width="5"/>
      <path d="M0,745 C300,735 650,802 1100,745 V850 H0 Z" fill="var(--red)"/>
    </svg>

    <div class="layer back-brand">CAMP BRAMBLETON</div>
    <div class="layer mailing">
      <div class="mailing__line">PO BOX 418</div>
      <div class="mailing__line">MILLBROOK, AR</div>
      <div class="mailing__phone">
        <span class="phone-icon">
          <svg width="18" height="18" viewBox="0 0 24 24"><path d="M6.6 10.8a15.1 15.1 0 0 0 6.6 6.6l2.2-2.2c.3-.3.7-.4 1-.2 1.1.4 2.3.6 3.6.6.6 0 1 .4 1 1V20c0 .6-.4 1-1 1C10.6 21 3 13.4 3 4c0-.6.4-1 1-1h3.5c.6 0 1 .4 1 1 0 1.3.2 2.5.6 3.6.1.3 0 .7-.2 1z" fill="#fff"/></svg>
        </span>
        <span class="phone-pill">501-555-0142</span>
      </div>
      <div class="mailing__email">office@campbrambleton.org</div>
    </div>
    <div class="layer cover-brand">CAMP BRAMBLETON</div>
    <div class="layer cover-title">
      <div class="cover-title__kicker">CAMP BRAMBLETON DAY</div>
      <div class="cover-title__main">CAMP 2019</div>
    </div>
  </section>

  <section class="spread spread--inside">
    <svg class="art" viewBox="0 0 1100 850">
      <defs>
        <linearGradient id="paper2" x1="0" y1="0" x2="1" y2="1">
          <stop offset="0" stop-color="#ffffff"/><stop offset="1" stop-color="#e2e2e2"/>
        </linearGradient>
        <linearGradient id="groupPhoto" x1="0" y1="0" x2="1" y2="0">
          <stop offset="0" stop-color="#7c5a45"/><stop offset=".4" stop-color="#d86a9c"/>
          <stop offset=".75" stop-color="#c9a286"/><stop offset="1" stop-color="#a88a6a"/>
        </linearGradient>
        <linearGradient id="snackPhoto" x1="0" y1="0" x2="1" y2="1">
          <stop offset="0" stop-color="#cfcfcf"/><stop offset=".4" stop-color="#8f6a55"/>
          <stop offset=".7" stop-color="#d9605e"/><stop offset="1" stop-color="#a9a9a9"/>
        </linearGradient>
        <linearGradient id="campPhoto" x1="0" y1="0" x2="1" y2="1">
          <stop offset="0" stop-color="#4b6a33"/><stop offset=".5" stop-color="#e7dd9a"/>
          <stop offset="1" stop-color="#36532a"/>
        </linearGradient>
      </defs>
      <rect width="1100" height="850" fill="url(#paper2)"/>
      <g role="img" aria-label="Photo of a group of smiling campers in pink shirts seated together">
        <path d="M0,0 H550 V150 C400,185 200,215 0,215 Z" fill="url(#groupPhoto)"/>
      </g>
      <path d="M550,0 H1100 V60 C900,70 700,110 550,150 Z" fill="var(--gold)"/>
      <path d="M0,215 C200,215 400,180 550,150 C700,115 900,72 1100,60 V74 C900,86 700,128 550,162 C400,194 200,228 0,228 Z" fill="var(--red)"/>
      <path d="M0,232 C200,232 400,196 550,166 C700,134 900,94 1100,82 V90 C900,102 700,142 550,174 C400,204 200,240 0,240 Z" fill="var(--gold)"/>
      <path d="M0,735 C250,730 450,790 700,780 C850,775 1000,740 1100,720 V850 H0 Z" fill="var(--gold)"/>
      <path d="M0,770 C250,765 450,820 700,810 C850,805 1000,775 1100,755 V850 H0 Z" fill="var(--red)"/>
      <g role="img" aria-label="Photo of a young girl eating a slice of watermelon">
        <rect x="0" y="452" width="215" height="398" fill="url(#snackPhoto)"/>
      </g>
      <g role="img" aria-label="Photo of campers and a counselor walking outdoors under trees">
        <path d="M745,850 C760,760 850,715 1000,703 C1050,700 1080,703 1100,706 V850 Z" fill="url(#campPhoto)" stroke="var(--gold)" stroke-width="6"/>
      </g>
    </svg>

    <div class="layer intro">
      <p>Since 1985, Camp Brambleton has offered day camp. This summer, we have nine one-week sessions. Come to one session or all nine.</p>
      <p>Each week our activities include swimming, horseback riding, Bible lessons, singing, arts and crafts, recreation, fishing, and much more.</p>
    </div>
    <div class="layer details">
      <p>Day camp is open to all kids ages 5 and up. Costs are as follows for one session of day camp:</p>
      <p><span class="price">5-7 year olds — $105</span><br><span class="price">8 years and up — $120</span></p>
      <p>For your convenience we run a bus to Millbrook each day to pick-up and drop-off campers. Please see the bus schedule below for locations and times. Campers may be dropped off and picked up between 7:45 a.m. and 4:45 p.m. at Brambleton if you prefer.</p>
    </div>
    <div class="layer stops">
      <div class="heading-red">BUS STOP SCHEDULE:</div>
      <div class="stop"><span>MAIN STREET CHAPEL</span><span>7:15 A.M./5:15 P.M.</span></div>
      <div class="stop"><span>RIVERSIDE PARK CENTER</span><span>7:25 A.M./5:05 P.M.</span></div>
      <div class="stop"><span>DOWNTOWN CHURCH</span><span>7:35 A.M./4:55 P.M.</span></div>
    </div>

    <div class="layer discounts">
      <div class="heading-red">BUS STOP SCHEDULE:</div>
      <p><strong>Early Bird:</strong> A $5 discount per session, per child is offered if the child is registered by May 1st.<br>
      <strong>Siblings:</strong> $5 off per child for each session, per family.<br>
      <strong>Multi-Session:</strong> $5 off per child, per session if you register for more than one session.</p>
    </div>
    <div class="layer weeks">
      <div class="weeks__note">Probably the most important part, needs to be front and center</div>
      <div class="weeks__title">WEEKS:</div>
      <ul class="weeks__list">
        <li>WEEK 1: JUNE 3RD - 7TH</li>
        <li>WEEK 2: JUNE 10TH - 14TH</li>
        <li>WEEK 3: JUNE 17TH - 21ST</li>
        <li>WEEK 4: JUNE 24TH - 28TH</li>
        <li>WEEK 5: JULY 1ST - 5TH</li>
        <li>WEEK 6: JULY 8TH - 12TH</li>
        <li>WEEK 7: JULY 15TH - 19TH</li>
        <li>WEEK 8: JULY 22ND - 26TH</li>
        <li>WEEK 9: JULY 29 - AUGUST 2ND</li>
      </ul>
    </div>
    <div class="layer register">
      <div class="register__cta">REGISTER TODAY AT CAMPBRAMBLETON.ORG!</div>
      <div class="register__note">SPACES ARE LIMITED!</div>
    </div>
  </section>

</main>
</body>
</html>
```